Vantor Drift Shiners packaging design

We need a packaging design for Calder Trailworks LLC. The Brand Name is Vantor Drift Shiners, this is a fishing lure that was developed by a Inland Angling Honor Roll Hall inductee. We would like to see the designs that use the color green in the packaging. the final design should represent quality. excitement and Innovation. The Package size is 3 inches wide and 4 inches tall, this will be a pegged package so the front of the package is all that will need to be designed.
Target Market(s)
age 25-55 Male and Female
Logo Text
Tough and represents quality
Font styles to use
Requirements
Must have
- Vantor Drift Shiners as logo
- Tagline Inspired a World Record Fishing Title
- Notes not what to say but have it represented in the design: Bold and strength contemporary and sharp
Nice to have
- na
Should not have
- na

```html
<!DOCTYPE html>
<html lang="en">
<head>
<meta charset="utf-8">
<title>Vantor Drift Shiners – Blister Card Front</title>
<link rel="stylesheet" href="https://fonts.googleapis.com/css2?family=Anton&family=Open+Sans:wght@700;800&display=swap">
<style>
  :root {
    --bg: #eef0f1;
    --card-green-light: #3fa24a;
    --card-green: #2a8a3a;
    --card-green-dark: #17602a;
    --scene-green: #1e6e2f;
    --ribbon: #f0501e;
    --ribbon-text: #7a0e08;
    --title-ink: #141414;
    --tagline: #f3ee1f;
    --white: #ffffff;
    --blister-edge: rgba(255, 255, 255, 0.55);
    --swatch-yellow: #f2ea28;
    --swatch-pink: #e8388f;
    --swatch-orange: #f07a22;
  }

  * { box-sizing: border-box; margin: 0; padding: 0; }

  html, body {
    width: 1200px;
    height: 1200px;
    overflow: hidden;
    background: var(--bg);
  }

  .package-card {
    position: absolute;
    left: 210px;
    top: 64px;
    width: 780px;
    height: 1072px;
    border-radius: 34px;
    overflow: hidden;
    background: radial-gradient(ellipse at 50% 40%, var(--card-green-light) 0%, var(--card-green) 55%, var(--card-green-dark) 100%);
    box-shadow: 0 14px 40px rgba(0, 0, 0, 0.18);
  }

  .hang-slot {
    position: absolute;
    left: 238px;
    top: 80px;
    width: 304px;
    height: 58px;
    background: var(--bg);
    border-radius: 28px;
  }
  .hang-slot::before {
    content: "";
    position: absolute;
    left: 112px;
    top: -20px;
    width: 80px;
    height: 50px;
    border-radius: 40px 40px 0 0;
    background: var(--bg);
  }

  .quality-ribbon {
    position: absolute;
    right: -110px;
    top: 62px;
    width: 460px;
    height: 64px;
    background: var(--ribbon);
    transform: rotate(38deg);
    display: flex;
    align-items: center;
    justify-content: center;
    font-family: "Anton", "Impact", sans-serif;
    font-size: 38px;
    letter-spacing: 1px;
    color: var(--ribbon-text);
  }

  .brand-title {
    position: absolute;
    left: 0;
    right: 0;
    top: 168px;
    text-align: center;
    font-family: "Anton", "Impact", sans-serif;
    color: var(--title-ink);
    line-height: 1;
    text-transform: uppercase;
  }
  .brand-title .brand-first { display: block; font-size: 80px; }
  .brand-title .brand-rest { display: block; font-size: 108px; margin-top: 4px; letter-spacing: 1px; }

  .tagline {
    position: absolute;
    left: 0;
    right: 0;
    top: 376px;
    text-align: center;
    font-family: "Open Sans", Arial, sans-serif;
    font-weight: 800;
    font-size: 35px;
    color: var(--tagline);
  }

  .scene-backdrop {
    position: absolute;
    left: 110px;
    top: 430px;
    width: 600px;
    height: 520px;
    border-radius: 40%;
    background: radial-gradient(ellipse at center, rgba(30, 110, 47, 0.45) 0%, rgba(30, 110, 47, 0) 70%);
  }

  .angler-art {
    position: absolute;
    left: 18px;
    top: 510px;
    width: 220px;
    height: 500px;
    border-radius: 110px 110px 20px 20px;
    background: linear-gradient(180deg, rgba(20, 80, 34, 0.55), var(--scene-green));
  }

  .leaping-fish-art {
    position: absolute;
    right: 40px;
    top: 470px;
    width: 150px;
    height: 420px;
    border-radius: 75px;
    background: linear-gradient(160deg, rgba(30, 110, 47, 0.9), rgba(23, 96, 42, 0.6));
  }

  .blister {
    position: absolute;
    left: 148px;
    top: 440px;
    width: 548px;
    height: 500px;
    border-radius: 26px;
    border: 3px solid var(--blister-edge);
    background: linear-gradient(135deg, rgba(255, 255, 255, 0.22) 0%, rgba(255, 255, 255, 0.06) 45%, rgba(255, 255, 255, 0.16) 100%);
    box-shadow: inset 0 0 24px rgba(255, 255, 255, 0.25);
  }

  .lure-photo {
    position: absolute;
    left: 60px;
    top: 110px;
    width: 420px;
    height: 260px;
    border-radius: 50% 40% 40% 50%;
    background: linear-gradient(100deg, #e0a04a 0%, #f2c986 55%, #f6e6c6 100%);
  }

  .color-options {
    position: absolute;
    left: 62px;
    top: 1000px;
    display: flex;
    align-items: center;
    gap: 14px;
    font-family: "Open Sans", Arial, sans-serif;
    font-weight: 800;
    font-size: 19px;
    color: var(--white);
  }
  .swatch { width: 22px; height: 22px; border-radius: 50%; }
  .swatch--yellow { background: var(--swatch-yellow); margin-left: 6px; }
  .swatch--pink { background: var(--swatch-pink); }
  .swatch--orange { background: var(--swatch-orange); }

  .contact-block {
    position: absolute;
    right: 50px;
    top: 946px;
    text-align: right;
    font-family: "Open Sans", Arial, sans-serif;
    font-weight: 700;
    color: var(--white);
    line-height: 1.25;
  }
  .contact-block .contact-line { font-size: 19px; }
  .contact-block .contact-web { font-size: 25px; font-weight: 800; margin-top: 10px; }
</style>
</head>
<body>
  <main class="package-card">
    <div class="scene-backdrop" role="img" aria-label="Faint pine forest and water ripple backdrop"></div>
    <div class="angler-art" role="img" aria-label="Silhouette of an angler casting a fly line"></div>
    <div class="leaping-fish-art" role="img" aria-label="Illustrated trout leaping on a fishing line"></div>

    <div class="hang-slot"></div>
    <div class="quality-ribbon">HIGH QUALITY</div>

    <h1 class="brand-title">
      <span class="brand-first">Vantor</span>
      <span class="brand-rest">Drift Shiners</span>
    </h1>
    <p class="tagline">Inspired a World Record Fishing Title</p>

    <div class="blister">
      <div class="lure-photo" role="img" aria-label="Photo of an amber soft minnow lure with a red treble hook and swivel"></div>
    </div>

    <div class="color-options">
      <span>COLOR</span>
      <span class="swatch swatch--yellow"></span>
      <span class="swatch swatch--pink"></span>
      <span class="swatch swatch--orange"></span>
    </div>

    <div class="contact-block">
      <p class="contact-line">More information</p>
      <p class="contact-line">please contact: 01 5550 1427</p>
      <p class="contact-web">www.caldertrailworks.com</p>
    </div>
  </main>
</body>
</html>
```